Northway Trade Partners Needs a FRESH website

We would like a creative minded designer to take on the task to Re-design our website. Its a simple 5-7 pages. With no cart, no complex html. Just plain information about our company and products we import and export. Pictures added to the product section. Since Our logo its Blue, we would like the designer to use complementing colors in order to make the website look cleaner and modern.

Target Market(s)

The target audience will be companies looking to purchase plastic related products. Companies looking to purchase large quantities of plastic containers (Shampoo bottles, caps, sprayers, mist sprayers, cosmetic containers etc).

Industry/Entity Type

It Company

Font styles to use
Sans Serif

Requirements
Must have
• We have a section in which we would like to add pictures of some of the products we carry, therefore having an easy and clean way to navigate through the pictures will be a plus.

```html
<!DOCTYPE html>
<html lang="en">
<head>
<meta charset="utf-8">
<title>Northway Trade Partners</title>
<link rel="stylesheet" href="https://fonts.googleapis.com/css2?family=Ubuntu:wght@400;500;700&family=Open+Sans:wght@400;600&display=swap">
<style>
:root{
  --blue:#0a78d0;
  --blue-bright:#1a85d8;
  --blue-dark:#0862ac;
  --blue-deep:#06528f;
  --blue-line:#4ea3e6;
  --title-blue:#1677c8;
  --ink:#333;
  --grey:#6f6f6f;
  --grey-light:#8a8a8a;
  --page:#f6f6f6;
  --white:#fff;
  --rule:#dcdcdc;
}
*{box-sizing:border-box;margin:0;padding:0}
html,body{width:1200px;height:2835px;overflow:hidden}
body{position:relative;background:var(--page);font-family:"Open Sans",sans-serif;color:var(--ink)}
.abs{position:absolute}
a{color:inherit;text-decoration:none}

/* top bar */
.topbar{left:0;top:0;width:1200px;height:73px;background:var(--blue)}
.social{display:flex;gap:6px}
.social span{width:24px;height:24px;border-radius:50%;background:var(--white);display:block}
.topbar .social{position:absolute;left:833px;top:24px}
.search{position:absolute;left:940px;top:23px;width:210px;height:26px;border-radius:13px;background:var(--white);font-size:12px;color:#9a9a9a;padding:4px 12px;font-style:italic}
.search svg{position:absolute;right:10px;top:6px}

/* header */
.header{left:0;top:73px;width:1200px;height:139px;background:var(--page);border-bottom:1px solid #e2e2e2;box-shadow:0 2px 4px rgba(0,0,0,.06)}
.brand{position:absolute;left:86px;top:-44px;width:210px;text-align:center}
.brand-mark{width:96px;height:96px;border-radius:50%;background:var(--blue-bright);border:4px solid var(--white);margin:0 auto}
.brand-name{font-family:"Ubuntu",sans-serif;font-weight:500;font-size:24px;line-height:27px;color:var(--title-blue);margin-top:6px}
.nav{position:absolute;top:63px;font-family:"Ubuntu",sans-serif;font-size:14px;letter-spacing:1px;color:#444}

/* hero */
.hero{left:0;top:213px;width:1200px;height:475px;background:linear-gradient(180deg,#f1f1f1,#e3e3e3)}
.hero-title{left:129px;top:98px;font-family:"Ubuntu",sans-serif;font-weight:700;font-size:29px;letter-spacing:1px;color:var(--title-blue)}
.hero-lead{left:131px;top:136px;width:520px;font-family:"Ubuntu",sans-serif;font-size:24px;line-height:29px;color:#3a3a3a}
.hero-text{left:131px;top:205px;width:490px;font-size:15px;line-height:23px;color:var(--grey-light)}
.pill{top:298px;height:37px;border-radius:19px;background:linear-gradient(180deg,#2a95e4,#0a6fc2);border:2px solid #07508c;color:var(--white);font-size:13px;line-height:33px;text-align:center}
.hero-visual{left:736px;top:52px;width:464px;height:423px;background:radial-gradient(circle at 40% 38%,#bfe6ff 0,#4cb3f2 28%,#9ccbe6 42%,rgba(220,190,170,.55) 62%,rgba(230,230,230,0) 78%)}

/* section headings */
.heading{font-family:"Ubuntu",sans-serif;font-weight:500;font-size:19px;color:#555}
.heading b{font-weight:500;color:var(--title-blue)}
.rule{height:1px;background:var(--rule)}
.rule-accent{height:6px;background:var(--blue-bright)}

/* offer */
.offer{left:0;top:688px;width:1200px;height:654px}
.dots{left:1048px;top:86px;display:flex;gap:4px}
.dots span{width:11px;height:11px;border-radius:50%;background:#b9b9b9}
.dots span:first-child{background:var(--blue)}
.service-box{width:135px;height:116px;border-radius:4px;background:linear-gradient(180deg,#fbfbfb,#e6e6e6);border:1px solid #dedede;border-bottom:5px solid #a9a9a9;display:flex;align-items:center;justify-content:center}
.service-title{font-family:"Ubuntu",sans-serif;font-size:16px;letter-spacing:.5px;color:var(--title-blue)}
.service-text{width:250px;font-size:14px;line-height:19px;color:var(--grey)}

/* welcome */
.welcome{left:0;top:1342px;width:1200px;height:516px;background:var(--blue)}
.notch{left:581px;top:0}
.welcome .heading{color:var(--white)}
.welcome .rule{background:var(--blue-line);opacity:.6}
.welcome .rule-accent{background:var(--blue-line)}
.team-photo{left:98px;top:179px;width:377px;height:248px;border:4px solid var(--blue-deep);background:linear-gradient(135deg,#e9eef2,#c9d3dc 45%,#8c9bab 75%,#3e4a58)}
.welcome-text{left:529px;top:179px;width:570px;font-size:15px;line-height:23px;color:var(--white)}

/* news */
.news{left:0;top:1858px;width:1200px;height:536px}
.port-photo{left:88px;top:161px;width:312px;height:202px;border:3px solid #e6e6e6;background:linear-gradient(180deg,#d9dde0 0,#a9b7c3 30%,#6d7c88 55%,#8a5d48 75%,#4c5a66)}
.btn{top:382px;height:37px;color:var(--white);font-size:13px;letter-spacing:.5px;line-height:37px;text-align:center}
.btn-blue{background:var(--blue)}
.btn-dark{background:#474747;border-bottom:3px solid #2e2e2e}
.article{width:290px}
.article-icon{position:absolute;left:0;top:2px}
.article-title{margin-left:35px;font-family:"Ubuntu",sans-serif;font-size:15px;color:var(--title-blue);letter-spacing:.3px}
.article-text{margin-left:35px;margin-top:3px;font-size:13px;line-height:21px;color:var(--grey)}
.article-more{margin-left:35px;font-size:13px;line-height:21px;color:var(--title-blue)}

/* footer */
.footer-band{left:0;top:2394px;width:1200px;height:45px;background:var(--blue-bright)}
.footer{left:0;top:2439px;width:1200px;height:349px;background:var(--blue)}
.footer-title{font-family:"Ubuntu",sans-serif;font-weight:500;font-size:16px;letter-spacing:.5px;color:var(--white)}
.sublinks{list-style:none}
.sublinks li{height:36px;border-bottom:1px solid rgba(255,255,255,.15);font-size:15px;color:var(--white);line-height:26px}
.sublinks li::before{content:"›";font-weight:700;margin-right:4px}
.sub-note{font-size:13px;color:var(--white)}
.field{width:185px;height:30px;background:var(--white);font-size:13px;color:#666;padding:6px 8px}
.submit{width:121px;height:31px;background:var(--blue-deep);color:var(--white);font-size:13px;letter-spacing:.5px;text-align:center;line-height:31px}
.footer-brand{left:911px;top:51px;width:178px;text-align:center}
.footer-brand .mark{width:72px;height:72px;border-radius:50%;background:var(--white);margin:0 auto}
.footer-brand .name{font-family:"Ubuntu",sans-serif;font-weight:500;font-size:21px;line-height:24px;color:var(--white);margin-top:6px}
.footer .social{position:absolute;left:955px;top:201px;gap:12px}
.bottombar{left:0;top:2788px;width:1200px;height:47px;background:var(--blue-dark);color:var(--white);font-size:12px;line-height:47px}
</style>
</head>
<body>

<div class="abs topbar">
  <div class="social"><span></span><span></span><span></span></div>
  <div class="search">Keyword Search...
    <svg width="14" height="14" viewBox="0 0 14 14"><circle cx="5.5" cy="5.5" r="4" fill="none" stroke="#999" stroke-width="1.8"/><line x1="8.5" y1="8.5" x2="13" y2="13" stroke="#999" stroke-width="2"/></svg>
  </div>
</div>

<header class="abs header">
  <div class="brand">
    <div class="brand-mark"></div>
    <div class="brand-name">Northway Trade<br>Partners</div>
  </div>
  <nav>
    <a class="nav" style="left:400px">HOME</a>
    <a class="nav" style="left:512px">WHO WE ARE</a>
    <a class="nav" style="left:675px">WHAT WE OFFER</a>
    <a class="nav" style="left:862px">MARKETS WE SERVE</a>
    <a class="nav" style="left:1071px">CONTACT</a>
  </nav>
</header>

<section class="abs hero">
  <h1 class="abs hero-title">YOU DREAM IT &nbsp;AND WE DELIVER IT</h1>
  <p class="abs hero-lead">Lorem ipsum dolor sit amet consec tetur adipiscing elit sed non odio lorem felis</p>
  <p class="abs hero-text">Lorem ipsum dolor sit amet, consectetur adipiscing elit. Sed non odio lorem. Pellentesque nec lacinia felis. Morbi sed est posuere orci faucibus feugiat a vitae quam.</p>
  <a class="abs pill" style="left:131px;width:131px">More details +</a>
  <a class="abs pill" style="left:277px;width:131px">Contact us ✉</a>
  <div class="abs hero-visual" role="img" aria-label="Glowing blue globe held in an open hand"></div>
</section>

<section class="abs offer">
  <h2 class="abs heading" style="left:92px;top:58px">What we <b>offer</b></h2>
  <div class="abs dots"><span></span><span></span><span></span></div>
  <div class="abs rule" style="left:92px;top:105px;width:1000px"></div>
  <div class="abs rule-accent" style="left:92px;top:102px;width:66px"></div>

  <div class="abs service-box" style="left:127px;top:168px">
    <svg width="60" height="60" viewBox="0 0 60 60"><circle cx="25" cy="25" r="15" fill="none" stroke="#1677c8" stroke-width="5"/><line x1="36" y1="36" x2="52" y2="52" stroke="#1677c8" stroke-width="7" stroke-linecap="round"/></svg>
  </div>
  <h3 class="abs service-title" style="left:281px;top:170px">PRODUCT RESEARCH</h3>
  <p class="abs service-text" style="left:281px;top:194px">Lorem ipsum dolor sit amet con sectetur adip iscing elit. Sed non odio lorem pellentesque. Iacinia felis. Morbi sed est posuere orci.</p>

  <div class="abs service-box" style="left:637px;top:168px">
    <svg width="76" height="60" viewBox="0 0 76 60" fill="none" stroke="#1677c8" stroke-width="3.5"><rect x="4" y="14" width="40" height="30" rx="3"/><path d="M44 24h14l10 12v8H44z"/><circle cx="18" cy="48" r="6" fill="#fff"/><circle cx="56" cy="48" r="6" fill="#fff"/><circle cx="18" cy="14" r="11" fill="#fff"/><path d="M18 8v6l4 3"/></svg>
  </div>
  <h3 class="abs service-title" style="left:790px;top:170px">DELIVERY</h3>
  <p class="abs service-text" style="left:790px;top:194px">Lorem ipsum dolor sit amet con sectetur adip iscing elit. Sed non odio lorem pellentesque. Iacinia felis. Morbi sed est posuere orci.</p>

  <div class="abs service-box" style="left:127px;top:372px">
    <svg width="74" height="50" viewBox="0 0 74 50" fill="#1677c8"><path d="M4 26c10-4 40-8 62-10 4 0 6 3 2 5-14 6-40 12-60 12z"/><path d="M30 20l-8-16h8l18 14z"/><path d="M28 30l-6 14h8l14-16z"/><path d="M4 22l-2-10h5l8 10z"/><rect x="46" y="34" width="20" height="3"/><rect x="50" y="40" width="16" height="3"/></svg>
  </div>
  <h3 class="abs service-title" style="left:281px;top:374px">FREIGHT FORWARDING</h3>
  <p class="abs service-text" style="left:281px;top:398px">Lorem ipsum dolor sit amet con sectetur adip iscing elit. Sed non odio lorem pellentesque. Iacinia felis. Morbi sed est posuere orci.</p>

  <div class="abs service-box" style="left:637px;top:372px">
    <svg width="56" height="56" viewBox="0 0 56 56" fill="none" stroke="#1677c8" stroke-width="3.5" stroke-linejoin="round"><path d="M28 4l22 10v26L28 52 6 40V14z"/><path d="M6 14l22 12 22-12M28 26v26"/><path d="M16 9l22 11" /><path d="M28 26l22-12v26L28 52z" fill="#1677c8"/></svg>
  </div>
  <h3 class="abs service-title" style="left:790px;top:374px">PACKAGING</h3>
  <p class="abs service-text" style="left:790px;top:398px">Lorem ipsum dolor sit amet con sectetur adip iscing elit. Sed non odio lorem pellentesque. Iacinia felis. Morbi sed est posuere orci.</p>
</section>

<section class="abs welcome">
  <svg class="abs notch" width="38" height="27" viewBox="0 0 38 27"><path d="M0 0h38L19 27z" fill="#f6f6f6"/></svg>
  <h2 class="abs heading" style="left:92px;top:75px">Welcome to Northway Trade Partners</h2>
  <div class="abs rule" style="left:92px;top:125px;width:1000px"></div>
  <div class="abs rule-accent" style="left:92px;top:122px;width:66px"></div>
  <div class="abs team-photo" role="img" aria-label="Group of smiling business professionals standing together"></div>
  <div class="abs welcome-text">
    <p>Northway Trade Partners will be your first and last stop for sourcing products from all over the world, specifically Asia and South America. We have partners all around the globe that helps us make the best decision in sourcing a product from and to any market.<br>Northway Trade Partners will always make the right choice for our clients when dealing with factories all over the world.</p>
    <p style="margin-top:32px">We at Northway Trade Partners have a great relationship with our suppliers which leads us to become more efficient at sourcing products and delivering it to our clients.</p>
  </div>
</section>

<section class="abs news">
  <h2 class="abs heading" style="left:92px;top:70px">News <b>Update</b></h2>
  <div class="abs rule" style="left:92px;top:118px;width:1000px"></div>
  <div class="abs rule-accent" style="left:92px;top:115px;width:66px"></div>
  <div class="abs port-photo" role="img" aria-label="Container port with stacked shipping containers and cranes"></div>
  <a class="abs btn btn-blue" style="left:88px;width:164px">VIEW ALL ARTICLES</a>
  <a class="abs btn btn-dark" style="left:265px;width:137px">CONTACT US</a>

  <div class="abs" style="left:744px;top:161px;width:1px;height:279px;background:var(--rule)"></div>
  <div class="abs rule" style="left:438px;top:290px;width:292px"></div>
  <div class="abs rule" style="left:760px;top:290px;width:310px"></div>
  <div class="abs rule" style="left:88px;top:457px;width:981px"></div>

  <article class="abs article" style="left:438px;top:174px">
    <svg class="article-icon" width="28" height="30" viewBox="0 0 28 30" fill="none" stroke="#1677c8" stroke-width="2"><path d="M3 2h13l6 6v10M3 2v24h11"/><path d="M7 10h9M7 14h9M7 18h5"/><circle cx="21" cy="23" r="6" fill="#fff"/><path d="M18 23l2 2 4-4"/></svg>
    <h3 class="article-title">TITLE OF THE ARTICLE GOES HERE</h3>
    <p class="article-text">Lorem ipsum dolor sit amet, consectetur adipiscing elit. Phasellus tincidunt tellus leo, sodales vestibulum urna.</p>
    <a class="article-more">Read more →</a>
  </article>
  <article class="abs article" style="left:769px;top:174px">
    <svg class="article-icon" width="28" height="30" viewBox="0 0 28 30" fill="none" stroke="#1677c8" stroke-width="2"><path d="M3 2h13l6 6v10M3 2v24h11"/><path d="M7 10h9M7 14h9M7 18h5"/><circle cx="21" cy="23" r="6" fill="#fff"/><path d="M18 23l2 2 4-4"/></svg>
    <h3 class="article-title">TITLE OF THE ARTICLE GOES HERE</h3>
    <p class="article-text">Lorem ipsum dolor sit amet, consectetur adipiscing elit. Phasellus tincidunt tellus leo, sodales vestibulum urna.</p>
    <a class="article-more">Read more →</a>
  </article>
  <article class="abs article" style="left:438px;top:317px">
    <svg class="article-icon" width="28" height="30" viewBox="0 0 28 30" fill="none" stroke="#1677c8" stroke-width="2"><path d="M3 2h13l6 6v10M3 2v24h11"/><path d="M7 10h9M7 14h9M7 18h5"/><circle cx="21" cy="23" r="6" fill="#fff"/><path d="M18 23l2 2 4-4"/></svg>
    <h3 class="article-title">TITLE OF THE ARTICLE GOES HERE</h3>
    <p class="article-text">Lorem ipsum dolor sit amet, consectetur adipiscing elit. Phasellus tincidunt tellus leo, sodales vestibulum urna.</p>
    <a class="article-more">Read more →</a>
  </article>
  <article class="abs article" style="left:769px;top:317px">
    <svg class="article-icon" width="28" height="30" viewBox="0 0 28 30" fill="none" stroke="#1677c8" stroke-width="2"><path d="M3 2h13l6 6v10M3 2v24h11"/><path d="M7 10h9M7 14h9M7 18h5"/><circle cx="21" cy="23" r="6" fill="#fff"/><path d="M18 23l2 2 4-4"/></svg>
    <h3 class="article-title">TITLE OF THE ARTICLE GOES HERE</h3>
    <p class="article-text">Lorem ipsum dolor sit amet, consectetur adipiscing elit. Phasellus tincidunt tellus leo, sodales vestibulum urna.</p>
    <a class="article-more">Read more →</a>
  </article>
</section>

<div class="abs footer-band"></div>
<footer class="abs footer">
  <h4 class="abs footer-title" style="left:133px;top:47px">Who we are</h4>
  <ul class="abs sublinks" style="left:133px;top:108px;width:175px">
    <li>Sublink here</li><li>Sublink here</li><li>Sublink here</li><li>Sublink here</li>
  </ul>
  <h4 class="abs footer-title" style="left:392px;top:47px">What we offer</h4>
  <ul class="abs sublinks" style="left:392px;top:108px;width:185px">
    <li style="height:39px">Sublink here</li><li style="height:39px">Sublink here</li><li style="height:39px">Sublink here</li><li style="height:39px">Sublink here</li>
  </ul>
  <h4 class="abs footer-title" style="left:648px;top:47px">Newsletter Signup</h4>
  <p class="abs sub-note" style="left:648px;top:112px">Subscribe to get updates</p>
  <div class="abs field" style="left:648px;top:142px">Email address</div>
  <div class="abs submit" style="left:648px;top:184px">SUBMIT</div>
  <div class="abs footer-brand">
    <div class="mark"></div>
    <div class="name">Northway Trade<br>Partners</div>
  </div>
  <div class="social"><span></span><span></span><span></span></div>
</footer>

<div class="abs bottombar">
  <span class="abs" style="left:129px">Copyright © 2014 Northway Trade Partners</span>
  <span class="abs" style="left:906px;width:204px;text-align:right">FAQ &nbsp;- &nbsp;Sitemap &nbsp;- &nbsp;Privacy Policy</span>
</div>

</body>
</html>
```